Webbanner-Design für Webradio Moderator
Zielgruppe
Ich bin ein Webradio Moderator. Ich unterhalte die Zuhörer mit einem bunten Music Mix und Ihren Wünschen.
Die Zielgruppe sind Leute die mein Werbe Banner dann sehen und Anhand dessen zu unserm Webradio kommen und uns zuhören.
I'm a Webradio moderator. I'm entertaining the audience with a colorful music mix and your wishes.
The target group are people who see my advertising banner and then come to our own Webradio and listen to us.
Aufgabenstellung
Es sollte so gestaltet sein, dass man genau weis um was es geht.
Eine gute Mischung das es nicht zu viel Bild neben dem Text ist aber auch nicht zu wenig.
Es sollte im Style wie der Banner 'wildtommi_show.jpg' unten etwa sein.
It should be designed to be exactly a point about what it is.
A good mix that does not take too much image next to the text is not too little.
It should be at the style like the banner'wildtommi _ show. jpg down.

```html
<!DOCTYPE html>
<html lang="de">
<head>
<meta charset="utf-8">
<title>Wild Tommi – On Air</title>
<link rel="stylesheet" href="https://fonts.googleapis.com/css2?family=Anton&family=Roboto:wght@900&family=Russo+One&display=swap">
<style>
  :root {
    --bg: #050507;
    --art-warm: #4a1a0a;
    --art-mid: #1c0d08;
    --art-cool: #0b0e1c;
    --onair-red: #ff2a1a;
    --onair-box: #1a0f0f;
    --onair-frame: #6e6e6e;
    --white: #ffffff;
    --play-top: #8ee04a;
    --play-bottom: #3fa51c;
    --play-edge: #2f7d12;
    --portrait-green: #5e9a24;
    --portrait-dark: #1d3a0c;
  }
  * { margin: 0; padding: 0; box-sizing: border-box; }
  html, body { width: 1200px; height: 676px; overflow: hidden; background: var(--bg); }
  .banner {
    position: relative;
    width: 1200px;
    height: 676px;
    overflow: hidden;
    background: var(--bg);
  }
  .soundwave-art {
    position: absolute;
    left: 0;
    top: 0;
    width: 880px;
    height: 676px;
    background: linear-gradient(90deg, var(--art-warm) 0%, var(--art-mid) 45%, var(--art-cool) 100%);
  }
  .host-portrait {
    position: absolute;
    right: 0;
    top: 0;
    width: 400px;
    height: 676px;
    background: linear-gradient(90deg, var(--art-cool) 0%, var(--portrait-green) 45%, var(--portrait-dark) 100%);
  }
  .on-air-sign {
    position: absolute;
    left: 468px;
    top: 10px;
    width: 250px;
    height: 92px;
    border: 6px solid var(--onair-frame);
    border-radius: 4px;
    background: var(--onair-box);
    display: flex;
    align-items: center;
    justify-content: center;
    box-shadow: inset 0 0 0 3px #2b2b2b;
  }
  .on-air-label {
    font-family: "Russo One", sans-serif;
    font-size: 50px;
    color: var(--onair-red);
    letter-spacing: 1px;
    text-shadow: 0 0 10px rgba(255,42,26,0.7);
  }
  .host-name {
    position: absolute;
    left: 0;
    top: 118px;
    width: 1200px;
    text-align: center;
    font-family: "Anton", sans-serif;
    font-weight: 400;
    color: var(--white);
    text-transform: uppercase;
    line-height: 1;
  }
  .host-name__first { display: block; font-size: 156px; letter-spacing: 6px; }
  .host-name__last { display: block; font-size: 172px; letter-spacing: 8px; margin-top: 6px; }
  .play-button {
    position: absolute;
    left: 360px;
    top: 496px;
    width: 490px;
    height: 88px;
    border-radius: 12px;
    border: 3px solid var(--play-edge);
    background: linear-gradient(to bottom, var(--play-top), var(--play-bottom));
    display: flex;
    align-items: center;
    justify-content: center;
    box-shadow: inset 0 2px 0 rgba(255,255,255,0.5);
  }
  .play-button__icon { position: absolute; left: 26px; top: 19px; }
  .play-button__label {
    font-family: "Roboto", sans-serif;
    font-weight: 900;
    font-size: 46px;
    color: var(--white);
    text-shadow: 0 2px 2px rgba(0,0,0,0.35);
  }
  .station-url {
    position: absolute;
    left: 0;
    top: 604px;
    width: 1200px;
    text-align: center;
    font-family: "Roboto", sans-serif;
    font-weight: 900;
    font-size: 47px;
    color: var(--white);
  }
</style>
</head>
<body>
  <div class="banner">
    <div class="soundwave-art" role="img" aria-label="Platz für die Grafik einer leuchtenden Schallplatte mit Audiowelle"></div>
    <div class="host-portrait" role="img" aria-label="Platz für das grün eingefärbte Foto des Moderators im Radiostudio"></div>

    <div class="on-air-sign"><span class="on-air-label">ON AIR</span></div>

    <h1 class="host-name">
      <span class="host-name__first">Wild</span>
      <span class="host-name__last">Tommi</span>
    </h1>

    <div class="play-button">
      <svg class="play-button__icon" width="40" height="46" viewBox="0 0 40 46" aria-hidden="true">
        <polygon points="2,2 38,23 2,44" fill="#ffffff"/>
      </svg>
      <span class="play-button__label">PLAY NOW</span>
    </div>

    <p class="station-url">www.klangwolkefunk.example</p>
  </div>
</body>
</html>
```